Website re-design for Birchmont LLC website ( has existing website )

Looking to do a complete re-design of Birchmontllc. The existing website is dated and built in wordpress. The new website will not be wordpress. The project folder includes an overview.txt file with details on the project. The file also contains a list of websites that he/she likes which I am sure is very helpful .
Number of Pages Required
1 page

```html
<!DOCTYPE html>
<html lang="en">
<head>
<meta charset="utf-8">
<title>Birchmont LLC</title>
<link href="https://fonts.googleapis.com/css2?family=Montserrat:wght@400;500;600;700;800&display=swap" rel="stylesheet">
<style>
:root{
  --blue:#0e5aa7;
  --blue-dark:#0a4a8c;
  --ink:#1c1c1c;
  --text:#333;
  --pale:#dbe8f6;
  --pale-2:#e8f0fa;
  --white:#fff;
  --black:#050505;
}
*{box-sizing:border-box;margin:0;padding:0}
html,body{width:1200px;height:4796px;overflow:hidden}
body{font-family:"Montserrat",Arial,sans-serif;color:var(--text);background:var(--white);position:relative}
.abs{position:absolute}
.btn{position:absolute;background:var(--blue);color:var(--white);font-weight:700;font-size:15px;display:flex;align-items:center;justify-content:center;border-radius:14px 3px 14px 3px;box-shadow:4px 4px 0 rgba(14,90,167,.25)}

/* top bar */
.topbar{position:absolute;left:0;top:0;width:1200px;height:37px;background:var(--blue);color:var(--white);font-size:15px}
.topbar .item{position:absolute;top:10px;display:flex;align-items:center;gap:9px}
.social{position:absolute;top:13px;display:flex;gap:17px;left:887px}
.social span{width:11px;height:11px;border-radius:50%;background:var(--white)}
.lang{position:absolute;left:1012px;top:9px;font-weight:700;font-size:14px;display:flex;gap:8px;align-items:center}

/* nav */
.nav{position:absolute;left:0;top:37px;width:1200px;height:90px;background:var(--white)}
.brand{position:absolute;display:flex;align-items:center;gap:10px;color:var(--blue);font-weight:500}
.brand .mark{border-radius:50%;background:var(--blue)}
.menu{position:absolute;left:373px;top:38px;display:flex;gap:19px;font-size:14px;color:var(--ink)}
.menu .active{color:var(--blue);font-weight:600;border-bottom:2px solid var(--blue);padding-bottom:3px}

/* hero */
.hero{position:absolute;left:0;top:127px;width:1200px;height:643px;background:linear-gradient(160deg,#2e4a23 0%,#3f5a2a 30%,#24361a 60%,#1b2a17 100%)}
.hero h1{position:absolute;left:93px;top:360px;font-size:42px;font-weight:800;color:var(--white);letter-spacing:.5px}
.hero p{position:absolute;left:95px;top:424px;font-size:16px;color:var(--white)}
.appt{position:absolute;left:727px;top:96px;width:383px;height:469px;background:rgba(14,90,167,.88);border-radius:28px 0 28px 0;color:var(--white);padding:0 35px}
.appt h3{text-align:center;font-size:17px;font-weight:700;margin-top:30px}
.field{position:absolute;font-size:11px}
.field .box{margin-top:11px;height:36px;border:1px solid rgba(255,255,255,.75)}
.submit{position:absolute;left:115px;top:366px;width:135px;height:40px;border:2px solid var(--white);border-radius:16px 3px 16px 3px;display:flex;align-items:center;justify-content:center;font-weight:700;font-size:15px}

/* about */
.about-frame{position:absolute;left:112px;top:857px;width:238px;height:266px;border:3px solid var(--blue)}
.about-photo{position:absolute;left:125px;top:870px;width:420px;height:363px;background:linear-gradient(180deg,#8aa5c2 0%,#6f88a4 45%,#4a5a68 100%);box-shadow:0 6px 18px rgba(0,0,0,.25)}
.eyebrow{position:absolute;left:616px;top:894px;font-size:16px;font-weight:700;color:var(--ink)}
.about h2{position:absolute;left:616px;top:930px;font-size:28px;font-weight:800;color:var(--ink);line-height:36px;width:470px}
.about h2 span{color:var(--blue)}
.about p{position:absolute;left:616px;top:1008px;width:472px;font-size:14px;line-height:25px;text-align:justify}

/* services */
.services{position:absolute;left:0;top:1317px;width:1200px;height:698px;background:linear-gradient(180deg,var(--pale) 0%,var(--pale-2) 100%)}
.sec-title{position:absolute;left:0;width:1200px;text-align:center;font-size:30px;font-weight:700;color:var(--blue)}
.sec-title::after{content:"";display:block;width:70px;height:3px;background:var(--blue);margin:10px auto 0}
.services .lead{position:absolute;top:155px;width:1200px;text-align:center;font-size:15px;color:var(--ink)}
.card{position:absolute;top:206px;width:225px;height:291px}
.card .photo{width:100%;height:100%}
.card .label{position:absolute;left:0;bottom:0;width:195px;height:45px;background:var(--white);display:flex;align-items:center;gap:12px;padding-left:8px;font-size:12px;font-weight:700;color:var(--blue)}
.card .label i{width:30px;height:30px;background:var(--pale);display:block;border-radius:3px}
.card.on .label{background:var(--blue);color:var(--white)}
.card.on .label i{background:var(--white)}

/* before/after */
.ba h3{position:absolute;font-size:32px;font-weight:700;color:var(--blue)}
.ba p{position:absolute;width:470px;font-size:14px;line-height:25px}
.circle{position:absolute;width:428px;height:428px;border-radius:50%;overflow:hidden;display:flex;gap:5px;background:var(--white)}
.circle .half{flex:1;display:flex;align-items:center;justify-content:center;color:var(--white);font-size:23px;font-weight:700}

/* testimonials */
.testi{position:absolute;left:0;top:3075px;width:1200px;height:589px;background:linear-gradient(180deg,var(--pale) 0%,var(--pale-2) 100%)}
.avatar{position:absolute;left:562px;top:236px;width:74px;height:74px;border-radius:50%;background:linear-gradient(180deg,#9aa5b0,#3c4650)}
.testi .name{position:absolute;top:334px;width:1200px;text-align:center;font-size:19px;font-weight:600;color:var(--ink)}
.testi .org{position:absolute;top:368px;width:1200px;text-align:center;font-size:19px;font-weight:700;color:var(--blue)}
.testi .quote{position:absolute;left:210px;top:402px;width:780px;text-align:center;font-size:14px;line-height:24px;color:var(--ink)}
.arrow{position:absolute;top:406px;width:40px;height:40px;border-radius:50%;background:var(--white);box-shadow:0 2px 6px rgba(0,0,0,.15);display:flex;align-items:center;justify-content:center}

/* gallery */
.tile{position:absolute}

/* footer */
.footer{position:absolute;left:0;top:4358px;width:1200px;height:438px;background:var(--black);color:var(--white)}
.fcol{position:absolute;top:68px}
.fcol h4{font-size:19px;font-weight:700;margin-bottom:14px}
.fcol li{list-style:none;font-size:14px;line-height:30px}
.news p{font-size:11px;line-height:20px;width:240px;margin-top:-4px}
.news .email{margin-top:14px;width:238px;height:31px;border:1px solid var(--white);font-size:11px;padding-left:10px;display:flex;align-items:center;position:relative}
.news .email b{position:absolute;right:0;top:0;width:34px;height:29px;background:var(--blue)}
.copy{position:absolute;top:380px;width:1200px;text-align:center;font-size:13px}
</style>
</head>
<body>

<div class="topbar">
  <div class="item" style="left:112px">
    <svg width="12" height="12" viewBox="0 0 24 24"><path fill="#fff" d="M6.6 10.8a15 15 0 0 0 6.6 6.6l2.2-2.2c.3-.3.7-.4 1-.2 1.1.4 2.3.6 3.6.6.6 0 1 .4 1 1V20c0 .6-.4 1-1 1A17 17 0 0 1 3 4c0-.6.4-1 1-1h3.5c.6 0 1 .4 1 1 0 1.3.2 2.5.6 3.6.1.3 0 .7-.2 1z"/></svg>
    612 555-0148
  </div>
  <div class="item" style="left:322px">
    <svg width="14" height="11" viewBox="0 0 24 18"><rect width="24" height="18" rx="2" fill="#fff"/><path d="M1 1l11 9 11-9" stroke="#0e5aa7" stroke-width="2" fill="none"/></svg>
    info@birchmontllc.in
  </div>
  <div class="social"><span></span><span></span><span></span><span></span></div>
  <div class="lang">
    <svg width="14" height="14" viewBox="0 0 24 24" fill="none" stroke="#fff" stroke-width="2"><circle cx="12" cy="12" r="10"/><path d="M2 12h20M12 2c3 3 3 17 0 20M12 2c-3 3-3 17 0 20"/></svg>
    <svg width="8" height="6" viewBox="0 0 8 6"><path d="M1 1l3 3 3-3" stroke="#fff" fill="none" stroke-width="1.5"/></svg>
    ENG
  </div>
</div>

<header class="nav">
  <div class="brand" style="left:112px;top:21px;font-size:27px"><span class="mark" style="width:52px;height:52px"></span>Birchmont</div>
  <nav class="menu">
    <span class="active">Home</span><span>About Us</span><span>Services</span><span>Employment</span><span>Testimonials</span><span>Gallery</span><span>FAQs</span>
  </nav>
  <div class="btn" style="left:954px;top:30px;width:134px;height:41px">Contact Us</div>
</header>

<section class="hero" role="img" aria-label="Two scuba divers wading through a lake covered in lily pads">
  <h1>RECLAIM OPEN WATER</h1>
  <p>Along your dock, beach, or boat slip</p>
  <div class="btn" style="left:93px;top:465px;width:134px;height:40px">Get Started</div>
  <form class="appt">
    <h3>Schedule An Appointment</h3>
    <div class="field" style="left:24px;top:73px;width:152px">Frist Name *<div class="box"></div></div>
    <div class="field" style="left:187px;top:73px;width:152px">Last Name *<div class="box"></div></div>
    <div class="field" style="left:24px;top:146px;width:152px">Pin Code *<div class="box"></div></div>
    <div class="field" style="left:187px;top:146px;width:152px">Phone Number *<div class="box"></div></div>
    <div class="field" style="left:24px;top:222px;width:315px">Email Address *<div class="box"></div></div>
    <div class="field" style="left:24px;top:302px;width:315px">Message *<div class="box"></div></div>
    <div class="submit">Submit</div>
  </form>
</section>

<section class="about">
  <div class="about-frame"></div>
  <div class="about-photo" role="img" aria-label="Divers clearing lake weeds beside a long white dock"></div>
  <div class="eyebrow">ABOUT US</div>
  <h2>AQUATIC INNOVATORS, <span>AT YOUR SERVICE</span></h2>
  <p>Birchmont LLC is a company formed in response to the increasing incidence of invasive species in Minnesota’s lakes and water systems. The impact of these fast-growing nuisances, inspired our venture to effectively control unwanted lake weeds. Birchmont, LLC help provide the enjoyable weed-free lake environment craved by water enthusiasts.</p>
  <div class="btn" style="left:616px;top:1177px;width:134px;height:40px">Read More</div>
</section>

<section class="services">
  <h2 class="sec-title" style="top:84px">SERVICES</h2>
  <p class="lead">We Know There Is No Life Like The Lake Life And We Are Dedicated To Keeping It That Way.</p>
  <div class="card" style="left:112px"><div class="photo" role="img" aria-label="Scuba diver swimming underwater" style="background:linear-gradient(180deg,#3d8fc4,#1a5c94)"></div><div class="label"><i></i>Lake Weed Removal</div></div>
  <div class="card" style="left:363px"><div class="photo" role="img" aria-label="Underwater weeds covered in zebra mussels" style="background:linear-gradient(180deg,#6fae3a,#3d7a25)"></div><div class="label"><i></i>Zebra Mussel Removal</div></div>
  <div class="card on" style="left:614px"><div class="photo" role="img" aria-label="Worker in protective suit cleaning a shoreline" style="background:linear-gradient(180deg,#8d9aa6,#3f4a52)"></div><div class="label"><i></i>Shoreline Cleanups</div></div>
  <div class="card" style="left:863px"><div class="photo" role="img" aria-label="Sanded beach with kayaks by the water" style="background:linear-gradient(180deg,#8ea3b0,#8a7258)"></div><div class="label"><i></i>Beach Sanding</div></div>
  <div class="btn" style="left:525px;top:536px;width:152px;height:40px">Other Services</div>
</section>

<section class="ba">
  <h3 style="left:112px;top:2218px">Lorem ipsum dolor</h3>
  <p style="left:112px;top:2270px">Lorem ipsum dolor sit amet, consectetur adipiscing elit, sed do eiusmod tempor incididunt ut labore et dolore magna aliqua. Ut enim ad minim veniam, quis nostrud exercitation ullamco laboris nisi ut aliquip ex ea commodo consequat.</p>
  <div class="btn" style="left:112px;top:2390px;width:134px;height:40px">Read More</div>
  <div class="circle" style="left:660px;top:2124px">
    <div class="half" role="img" aria-label="Lake shoreline before cleanup" style="background:#16191c">Before</div>
    <div class="half" role="img" aria-label="Lake shoreline after cleanup" style="background:#1c2024">After</div>
  </div>

  <div class="circle" style="left:110px;top:2557px">
    <div class="half" role="img" aria-label="Dock covered in lake weeds" style="background:linear-gradient(180deg,#9fb4c4,#6f6a55)"></div>
    <div class="half" role="img" aria-label="Clean wooden dock" style="background:linear-gradient(180deg,#4c6a3a,#9a9288)"></div>
  </div>
  <h3 style="left:616px;top:2651px">Lorem ipsum dolor</h3>
  <p style="left:616px;top:2703px">Lorem ipsum dolor sit amet, consectetur adipiscing elit, sed do eiusmod tempor incididunt ut labore et dolore magna aliqua. Ut enim ad minim veniam, quis nostrud exercitation ullamco laboris nisi ut aliquip ex ea commodo consequat.</p>
  <div class="btn" style="left:616px;top:2822px;width:134px;height:40px">Read More</div>
</section>

<section class="testi">
  <h2 class="sec-title" style="top:130px">TESTIMONIALS</h2>
  <div class="avatar" role="img" aria-label="Customer portrait"></div>
  <div class="name">Lake Harrow</div>
  <div class="org">Fernwood Shores Association</div>
  <p class="quote">Everyone used to jump off the water trampoline and instantly get tangled in lake weeds. We contacted Birchmont and their SCUBA divers have now been solving our problem for the past 4 years!”</p>
  <div class="arrow" style="left:108px"><svg width="8" height="12" viewBox="0 0 8 12"><path d="M6 1L1 6l5 5" stroke="#333" fill="none" stroke-width="1.5"/></svg></div>
  <div class="arrow" style="left:1050px"><svg width="8" height="12" viewBox="0 0 8 12"><path d="M2 1l5 5-5 5" stroke="#333" fill="none" stroke-width="1.5"/></svg></div>
</section>

<section class="gallery">
  <h2 class="sec-title" style="top:3744px">GALLERY</h2>
  <div class="tile" role="img" aria-label="Boat lift frame on a lake" style="left:112px;top:3843px;width:234px;height:210px;background:linear-gradient(180deg,#a9c3e0,#243f72)"></div>
  <div class="tile" role="img" aria-label="Sunset over a lake from a dock" style="left:355px;top:3843px;width:235px;height:210px;background:linear-gradient(180deg,#4d6f9a,#e0a35a 45%,#2a2c30)"></div>
  <div class="tile" role="img" aria-label="Worker installing a dock in deep blue water" style="left:599px;top:3843px;width:234px;height:428px;background:linear-gradient(180deg,#6fa2dc,#1e3f7a)"></div>
  <div class="tile" role="img" aria-label="Dock covered in pulled lake weeds" style="left:845px;top:3843px;width:243px;height:210px;background:linear-gradient(180deg,#b4c6d4,#6d7a50)"></div>
  <div class="tile" role="img" aria-label="Clean wooden dock among reeds" style="left:112px;top:4062px;width:234px;height:209px;background:linear-gradient(180deg,#8aa8b8,#a69a88)"></div>
  <div class="tile" role="img" aria-label="Calm lake with a swim platform" style="left:355px;top:4062px;width:235px;height:209px;background:linear-gradient(180deg,#c3cfdb,#4d5c70)"></div>
  <div class="tile" role="img" aria-label="Equipment trailer parked by trees" style="left:845px;top:4062px;width:243px;height:209px;background:linear-gradient(180deg,#8fb2da,#3b2a24)"></div>
</section>

<footer class="footer">
  <div class="brand" style="left:112px;top:134px;color:var(--white);font-size:34px"><span class="mark" style="width:66px;height:66px"></span>Birchmont</div>
  <div class="fcol" style="left:435px"><h4>Use Links</h4><ul><li>Home</li><li>Services</li><li>About Us</li><li>Contact Us</li><li>FAQs</li><li>Employment</li><li>Testimonials</li><li>Gallery</li></ul></div>
  <div class="fcol" style="left:610px"><h4>Help Links</h4><ul><li>Terms &amp; Conditions</li><li>Privacy Policy</li><li>&nbsp;Support</li></ul></div>
  <div class="fcol news" style="left:850px;top:64px"><h4>NewsLetters</h4>
    <p>Lorem ipsum dolor sit amet, adipiscing elit, sed do eiusmod .Lorem ipsum dolor sit</p>
    <div class="email">Email<b></b></div>
  </div>
  <div class="copy">© 2022 birchmontllc | All Rights Reserved</div>
</footer>

</body>
</html>
```